Velmora EIRL Business Card Design Project

We need a business card design for a New Business Intelligence Consultant. We bring a complete service to the client from first consulting meeting to help desk and system improvement.

I will upload the company logo and I like to use the logo colors on the card. Feel free to use all logo components on the design, for example one side with the black logo using complete card and the other side only the red shape (is an example, feel absolutely free :)).

The principal idea is to sell a professional service and a modern company.

Target Market(s)

IT Business Intelligence Clients

Industry/Entity Type

Professional Service

Requirements
Nice to have
• - Use the logo colors and minimize white sections.
- Rounded borders
Should not have
• I don't want to see any references to people working on a meeting or office photos or any computers related logos.

```html
<!DOCTYPE html>
<html lang="es">
<head>
<meta charset="utf-8">
<title>Velmora EIRL – Tarjeta de presentación</title>
<link rel="stylesheet" href="https://fonts.googleapis.com/css2?family=Arimo:wght@400;700&display=swap">
<style>
  :root{
    --bg:#1c1c1e;
    --card:#0b0b0c;
    --card-edge:#161618;
    --red:#e8202a;
    --grey:#a9aaac;
    --grey-dark:#6e6f72;
    --text:#d7d7d9;
    --text-dim:#a0a0a3;
    --ink:#1a1a1a;
  }
  *{margin:0;padding:0;box-sizing:border-box}
  html,body{width:1200px;height:984px;overflow:hidden;background:var(--bg)}
  body{font-family:"Arimo",Arial,sans-serif;display:flex;flex-direction:column;align-items:center;justify-content:center;gap:40px}
  .card{position:relative;width:760px;height:434px;border-radius:16px;overflow:hidden;
    background:linear-gradient(160deg,var(--card-edge),var(--card) 60%)}
  .card svg.shapes{position:absolute;inset:0}

  /* back */
  .back-brand{position:absolute;right:50px;top:170px;text-align:right}
  .brand-name{font-weight:700;color:var(--red);letter-spacing:1px}
  .back-brand .brand-name{font-size:80px;line-height:1}
  .back-rule{height:2px;background:var(--grey);margin:14px 0 10px auto;width:330px}
  .back-url{font-size:17px;letter-spacing:3px;color:var(--text)}

  /* front */
  .front-brand{position:absolute;left:60px;top:46px;display:flex;align-items:center;gap:12px}
  .front-brand .mark{width:30px;height:30px;background:var(--grey)}
  .front-brand .brand-name{font-size:40px;line-height:1}
  .name{position:absolute;left:70px;top:159px;font-size:28px;font-weight:700;color:var(--red);letter-spacing:1px;text-transform:uppercase;white-space:nowrap}
  .role{position:absolute;left:410px;top:201px;font-size:18px;color:var(--ink);white-space:nowrap}
  .address{position:absolute;left:40px;top:262px;font-size:17px;line-height:1.35;color:var(--text-dim);font-style:normal}
  .address strong{color:var(--text);font-weight:700}
  .contacts{position:absolute;left:430px;top:300px;list-style:none;font-size:19px;color:var(--text)}
  .contacts li{display:flex;align-items:center;gap:14px;height:30px;white-space:nowrap}
  .contacts svg{width:16px;height:16px;flex:none}
</style>
</head>
<body>

<section class="card card-back" aria-label="Reverso de la tarjeta">
  <div class="back-brand">
    <div class="brand-name">velmora</div>
    <div class="back-rule"></div>
    <div class="back-url">www.velmora.cl</div>
  </div>
</section>

<section class="card card-front" aria-label="Anverso de la tarjeta">
  <svg class="shapes" viewBox="0 0 760 434" aria-hidden="true">
    <polygon points="30,150 760,190 760,250 30,210" fill="var(--grey)"/>
    <polygon points="760,250 760,268 30,228 30,210" fill="var(--red)"/>
    <polygon points="640,170 760,176 760,190 660,184" fill="var(--grey-dark)"/>
  </svg>
  <div class="front-brand">
    <span class="mark"></span>
    <span class="brand-name">velmora</span>
  </div>
  <h1 class="name">Tomás Aranda V.</h1>
  <p class="role">| Gerente General</p>
  <address class="address">
    <strong>Velmora EIRL</strong><br>
    Av. Los Alerces 248<br>
    Of. 310. Providencia, Santiago.
  </address>
  <ul class="contacts">
    <li><svg viewBox="0 0 16 16"><rect x="1" y="3" width="14" height="11" rx="2" fill="var(--red)"/><rect x="4" y="6" width="8" height="2" fill="#0b0b0c"/></svg>+56 (9) 91847362</li>
    <li><svg viewBox="0 0 16 16"><rect x="1" y="3" width="14" height="10" rx="3" fill="var(--red)"/><polyline points="2,4 8,9 14,4" fill="none" stroke="#0b0b0c" stroke-width="1.4"/></svg>tomas@velmora.cl</li>
    <li><svg viewBox="0 0 16 16"><circle cx="8" cy="8" r="7" fill="var(--red)"/><ellipse cx="8" cy="8" rx="3" ry="7" fill="none" stroke="#0b0b0c" stroke-width="1"/><line x1="1" y1="8" x2="15" y2="8" stroke="#0b0b0c" stroke-width="1"/></svg>www.velmora.cl</li>
  </ul>
</section>

</body>
</html>
```